Dr Tasneer's Letterhead

I need a professional neat letterhead incorporating my professional information, university titles and qualifications. I have attached my 3 recent ones which contain all the necessary information that needs to be included. I am happy for the information to be a side bar left or right, or as a header/footer combination.

Hello all

I have now made a 2nd and 3rd prize so please submit

Reason: Now there is a 2nd and 3rd place so I can take 3 designs

Industry/Entity Type

University

```html
<!DOCTYPE html>
<html lang="en">
<head>
<meta charset="utf-8">
<title>Dr Idris Tasneer Letterhead</title>
<link rel="stylesheet" href="https://fonts.googleapis.com/css2?family=Pinyon+Script&family=Arimo:wght@400;700&display=swap">
<style>
  :root {
    --backdrop: #d9d9d9;
    --paper: #ffffff;
    --teal-light: #4fcfd6;
    --teal-dark: #2db6bf;
    --green: #23994a;
    --teal-text: #2aa9b4;
    --white: #ffffff;
    --mark: #dff3f4;
  }
  * { box-sizing: border-box; margin: 0; padding: 0; }
  html, body { width: 1200px; height: 900px; overflow: hidden; background: var(--backdrop); }
  .canvas { position: relative; width: 1200px; height: 900px; }
  .letterhead {
    position: absolute; left: 274px; top: 98px; width: 494px; height: 692px;
    background: var(--paper);
    font-family: "Arimo", Arial, sans-serif;
  }
  .header {
    position: absolute; left: 0; top: 0; width: 100%; height: 144px;
    background: linear-gradient(180deg, var(--teal-light), var(--teal-dark));
    border-bottom: 7px solid var(--green);
  }
  .name {
    position: absolute; left: 40px; top: 16px;
    font-family: "Pinyon Script", cursive;
    color: var(--white); font-size: 44px; line-height: 58px;
  }
  .contact {
    position: absolute; left: 250px; top: 18px; width: 230px;
    color: var(--white); font-size: 11px; font-weight: 700; line-height: 13px;
  }
  .contact .phones { margin-top: 16px; font-size: 15px; line-height: 17px; }
  .sidebar {
    position: absolute; left: 369px; top: 164px; width: 120px;
    color: var(--teal-text); font-size: 10.5px; line-height: 12.5px;
  }
  .sidebar h2 { color: var(--green); font-size: 10.5px; font-weight: 700; margin-bottom: 14px; }
  .sidebar p { margin-bottom: 12px; }
  .sidebar p.gap { margin-top: 24px; }
  .body-mark {
    position: absolute; left: 150px; top: 330px;
    font-family: "Pinyon Script", cursive;
    color: var(--mark); font-size: 40px;
  }
  .footer {
    position: absolute; left: 0; bottom: 0; width: 100%; height: 53px;
    background: var(--green);
  }
  .badges { position: absolute; right: 20px; top: 10px; display: flex; gap: 12px; }
</style>
</head>
<body>
<div class="canvas">
  <div class="letterhead">
    <header class="header">
      <div class="name">Dr.Idris<br>Tasneer</div>
      <div class="contact">
        <p>Suite 210/48 Larkspur Road, Fernhill 2190</p>
        <p>9 Calder Highway, Ashmore 2163</p>
        <p>14 Pelham Street, Brookvale 2760</p>
        <p class="phones">Tel: 95550142 / 95550187<br>Fax: 95550193</p>
      </div>
    </header>
    <div class="body-mark">Idris Tasneer</div>
    <aside class="sidebar">
      <h2>EDUCTION &amp;SERVICES</h2>
      <p>BSc Med, MBBS (Hons 1) HCU</p>
      <p>MSc, FRACS (Oto-HNS)</p>
      <p>Consultant ENT/Head and Neck Surgeon</p>
      <p>Eastbrook Cancer Centre</p>
      <p>Fernhill Hospital and Northgate Local Health District (NLHD)</p>
      <p class="gap">Senior Lecturer, Lakeside University (LU) &amp; Northgate University (NU)</p>
    </aside>
    <footer class="footer">
      <svg class="badges" width="104" height="24" viewBox="0 0 104 24" role="img" aria-label="Affiliated institution badges">
        <rect x="0" y="2" width="20" height="20" fill="#e9c46a"/>
        <rect x="38" y="2" width="20" height="20" fill="#c0392b"/>
        <rect x="78" y="2" width="24" height="20" fill="#f4f4f4"/>
      </svg>
    </footer>
  </div>
</div>
</body>
</html>
```